Web Design for Rubbish Removal Company

I am looking for a custom web design that is clean and modern which also has a professional trustworthy feel to it.
The website is http://www.kendrawaste.com.au/ and need:
1 x Front Page
1 x Location Page
Please keep the green colour scheme as this is the corporate colours but would like to steer away from the black.
Industry/Entity Type
It Company
Number of Pages Required
2 page
Font styles to use
Sans Serif
Requirements
Must have
- Clean & Professional
- Keep green colour scheme
Should not have
- Steer away from black
- not look like a template

```html
<!DOCTYPE html>
<html lang="en">
<head>
<meta charset="utf-8">
<title>Kendra Waste</title>
<link href="https://fonts.googleapis.com/css2?family=Raleway:wght@300;400;600;700&family=Open+Sans:wght@400;600;700&display=swap" rel="stylesheet">
<style>
:root{
  --green:#78bf3f;
  --heading:#2e2e2e;
  --muted:#8a8a8a;
  --body:#333;
  --soft-bg:#f8f8f8;
  --footer:#4b4b4b;
  --footer-base:#3b3b3b;
  --white:#fff;
}
*{margin:0;padding:0;box-sizing:border-box}
html,body{width:960px;height:1200px;overflow:hidden}
body{font-family:'Open Sans',sans-serif;color:var(--body);background:var(--white);position:relative}

.stats{position:absolute;left:0;top:0;width:960px;height:190px;background:var(--green)}
.stat{position:absolute;top:24px;width:272px;text-align:center;color:var(--white);font-family:'Raleway',sans-serif}
.stat svg{display:block;margin:0 auto;height:40px}
.stat-value{font-size:24px;font-weight:700;margin-top:22px;line-height:1}
.stat-label{font-size:20px;font-weight:300;margin-top:8px}
.stat-label b{font-weight:700}
.stat-divider{position:absolute;top:25px;width:1px;height:124px;background:rgba(255,255,255,.45)}

.section-title{position:absolute;left:0;width:960px;text-align:center;font-family:'Raleway',sans-serif;font-weight:600;font-size:19px;letter-spacing:.5px;color:var(--heading)}
.section-intro{position:absolute;left:0;width:960px;text-align:center;font-family:'Raleway',sans-serif;font-weight:400;font-size:11.5px;line-height:16px;color:var(--muted);letter-spacing:.3px}

.feature{position:absolute;width:250px;height:52px}
.feature-icon{position:absolute;left:0;top:0;width:51px;height:51px;border-radius:50%;background:var(--green)}
.feature-icon svg{position:absolute;left:14px;top:14px}
.feature-text{position:absolute;left:74px;top:10px;width:180px;font-size:11.5px;line-height:16px;letter-spacing:.4px;color:var(--body)}
.feature-text b{font-weight:700}

.testimonials{position:absolute;left:0;top:577px;width:960px;height:389px;background:var(--soft-bg)}
.quote{position:absolute;top:166px;width:316px}
.quote p{font-size:11.8px;line-height:16px;color:#333;letter-spacing:.2px}
.quote cite{display:block;margin-top:14px;font-style:normal;font-size:9.5px;letter-spacing:.5px;color:#777}
.slider-dots{position:absolute;top:323px;left:462px;display:flex;gap:3px}
.slider-dots span{width:10px;height:10px;border-radius:50%;border:1px solid var(--green)}
.slider-dots span.active{background:var(--green)}

.site-footer{position:absolute;left:0;top:966px;width:960px;height:195px;background:var(--footer);color:#eee}
.footer-heading{position:absolute;top:46px;font-size:12px;font-weight:700;letter-spacing:.5px;color:var(--white)}
.footer-list{position:absolute;top:80px;list-style:none;font-size:12px;line-height:24px;letter-spacing:.4px}
.footer-list li{position:relative;padding-left:20px}
.footer-list li::before{content:"›";position:absolute;left:0;color:var(--green);font-size:13px}
.contact-list{position:absolute;left:104px;top:80px;list-style:none;font-size:12px;line-height:24px}
.contact-list li{display:flex;align-items:center;gap:5px}
.social{position:absolute;left:104px;top:131px;display:flex;gap:9px}
.social span{width:8px;height:8px;border-radius:50%;background:#ddd}
.payments{position:absolute;left:598px;top:82px;display:flex;gap:7px}
.card{width:30px;height:20px;background:var(--white);font-size:8px;font-weight:700;color:var(--footer);display:flex;align-items:center;justify-content:center}
.copyright{position:absolute;left:0;top:1161px;width:960px;height:39px;background:var(--footer-base);color:#eee;font-size:12px;letter-spacing:.4px;text-align:center;line-height:39px}
</style>
</head>
<body>

<section class="stats">
  <div class="stat" style="left:71px">
    <svg viewBox="0 0 44 40" width="44" fill="none" stroke="#fff" stroke-width="1.6"><path d="M22 37 C8 26 3 19 3 12 A9 9 0 0 1 22 8 A9 9 0 0 1 41 12 C41 19 36 26 22 37Z"/></svg>
    <div class="stat-value">175</div>
    <div class="stat-label"><b>happy</b> clients</div>
  </div>
  <div class="stat-divider" style="left:343px"></div>
  <div class="stat" style="left:344px">
    <svg viewBox="0 0 40 40" width="40" fill="none" stroke="#fff" stroke-width="1.6"><path d="M3 20 L20 4 L37 20 M8 16 V37 H32 V16 M16 37 V25 H24 V37 M28 6 V12"/></svg>
    <div class="stat-value">68</div>
    <div class="stat-label"><b>objects</b> done</div>
  </div>
  <div class="stat-divider" style="left:615px"></div>
  <div class="stat" style="left:607px">
    <svg viewBox="0 0 40 40" width="40" fill="none" stroke="#fff" stroke-width="1.6"><path d="M20 3 L25 15 L38 15.5 L28 24 L31.5 37 L20 29.5 L8.5 37 L12 24 L2 15.5 L15 15Z"/></svg>
    <div class="stat-value">4,9</div>
    <div class="stat-label"><b>rating</b> on Reviewly</div>
  </div>
</section>

<h2 class="section-title" style="top:234px">WHY CHOOSE US?</h2>
<p class="section-intro" style="top:275px;left:230px;width:500px">Our team of professional and friendly rubbish removalists in Sydney take tremendous pride in their work. We're a local company who understands what the what the Sydney locals want.</p>

<div class="feature" style="left:104px;top:374px">
  <div class="feature-icon"><svg width="24" height="24" viewBox="0 0 24 24" fill="none" stroke="#fff" stroke-width="2"><path d="M3 8 H14 L12.5 20 H4.5Z" fill="#fff"/><path d="M20 3 L14 19 M12 20 Q16 22 20 19"/></svg></div>
  <div class="feature-text"><b>Same-day</b> rubbish and waste collection</div>
</div>
<div class="feature" style="left:360px;top:374px">
  <div class="feature-icon"><svg width="24" height="24" viewBox="0 0 24 24" fill="none" stroke="#fff" stroke-width="2"><path d="M3 8 H14 L12.5 20 H4.5Z" fill="#fff"/><path d="M20 3 L14 19 M12 20 Q16 22 20 19"/></svg></div>
  <div class="feature-text"><b>Free quote</b> provided with all enquiries</div>
</div>
<div class="feature" style="left:616px;top:374px">
  <div class="feature-icon"><svg width="24" height="24" viewBox="0 0 24 24" fill="none" stroke="#fff" stroke-width="2"><path d="M3 8 H14 L12.5 20 H4.5Z" fill="#fff"/><path d="M20 3 L14 19 M12 20 Q16 22 20 19"/></svg></div>
  <div class="feature-text">Over <b>10 years</b> in the rubbish removal trade</div>
</div>
<div class="feature" style="left:104px;top:457px">
  <div class="feature-icon"><svg width="24" height="24" viewBox="0 0 24 24" fill="none" stroke="#fff" stroke-width="2"><path d="M3 8 H14 L12.5 20 H4.5Z" fill="#fff"/><path d="M20 3 L14 19 M12 20 Q16 22 20 19"/></svg></div>
  <div class="feature-text" style="width:190px"><b>CHEAPEST PRICES</b> in Sydney</div>
</div>
<div class="feature" style="left:360px;top:457px">
  <div class="feature-icon"><svg width="24" height="24" viewBox="0 0 24 24" fill="none" stroke="#fff" stroke-width="2"><path d="M3 8 H14 L12.5 20 H4.5Z" fill="#fff"/><path d="M20 3 L14 19 M12 20 Q16 22 20 19"/></svg></div>
  <div class="feature-text" style="width:140px"><b>Over 10 years</b> in the rubbish removal trade</div>
</div>
<div class="feature" style="left:616px;top:457px">
  <div class="feature-icon"><svg width="24" height="24" viewBox="0 0 24 24" fill="none" stroke="#fff" stroke-width="2"><path d="M3 8 H14 L12.5 20 H4.5Z" fill="#fff"/><path d="M20 3 L14 19 M12 20 Q16 22 20 19"/></svg></div>
  <div class="feature-text">No job is too large, too small or too difficult</div>
</div>

<section class="testimonials">
  <h2 class="section-title" style="top:22px">WHAT CLIENTS SAY</h2>
  <p class="section-intro" style="top:62px">Below are just some of the happy customers we've serviced in the Sydney metro region.<br>If you would like direct references from customers we've serviced in the past, please call us on 0400 555 010</p>
  <blockquote class="quote" style="left:130px">
    <p>Excellent service; quote given on the spot for major clean-up of household throw-outs. The team provides quick, efficient and courteous removal! Very satisfied customer.</p>
    <cite>Mara Ellison - Bondi Beach, Residential Rubbish Removal</cite>
  </blockquote>
  <blockquote class="quote" style="left:513px">
    <p>Dean, sensational job as always, love how easy you make it look. Definitely won't hesitate in calling you again should either my family or friends need rubbish removed. Thanks again!</p>
    <cite>Mara Ellison - Bondi Beach, Residential Rubbish Removal</cite>
  </blockquote>
  <div class="slider-dots"><span class="active"></span><span></span><span></span></div>
</section>

<footer class="site-footer">
  <h3 class="footer-heading" style="left:104px">Contact Information</h3>
  <ul class="contact-list">
    <li><svg width="9" height="9" viewBox="0 0 10 10"><path d="M2 0.5 L4 3 L3 4 Q4 6 6 7 L7 6 L9.5 8 L8 9.5 Q3 9 0.5 2Z" fill="#78bf3f"/></svg>0400 555 010</li>
    <li><svg width="9" height="7" viewBox="0 0 10 8"><rect width="10" height="8" fill="#78bf3f"/><path d="M0 0 L5 4 L10 0" stroke="#4b4b4b" fill="none"/></svg>hello@kendrawaste.com.au</li>
  </ul>
  <div class="social"><span></span><span></span><span></span><span></span></div>

  <h3 class="footer-heading" style="left:361px">Menu</h3>
  <ul class="footer-list" style="left:361px"><li>About</li><li>Services</li><li>Locations</li></ul>
  <ul class="footer-list" style="left:481px"><li>Blog</li><li>FAQ's</li><li>Contact</li></ul>

  <h3 class="footer-heading" style="left:598px">Payment Methods</h3>
  <div class="payments"><span class="card">Vero</span><span class="card">Mondo</span><span class="card">Paylo</span></div>
</footer>
<div class="copyright">Copyright Kendra Waste. All rights reserved.</div>

</body>
</html>
```